we need a business card in yellow, green and black with rounded edges. We are in the Construction and Engineering business. I need the below info included:

Neil Barton
Summitrow Engineering & Construction, Inc.
4158 Harbor Vale Drive,
Lakemont, Ca 92018
714-555-0147 Office
714-555-0192 Cell
714-555-0163 Fax
nb@summitrowec.com

thanks for your help!

```html
<!DOCTYPE html>
<html lang="en">
<head>
<meta charset="utf-8">
<title>Summitrow Engineering &amp; Construction – Business Card</title>
<link rel="stylesheet" href="https://fonts.googleapis.com/css2?family=Comfortaa:wght@400;600&display=swap">
<style>
  :root {
    --ink: #111111;
    --card-black: #151515;
    --paper: #ffffff;
    --mist: #e9e9e9;
    --backdrop: #d9d6d0;
    --brand-green: #3fae49;
    --brand-yellow: #d8d624;
    --text-light: #f2f2f2;
  }
  * { margin: 0; padding: 0; box-sizing: border-box; }
  html, body { width: 1200px; height: 791px; overflow: hidden; }
  body {
    background: var(--backdrop);
    font-family: "Comfortaa", sans-serif;
    position: relative;
  }
  .card {
    position: absolute;
    width: 500px;
    height: 286px;
    border-radius: 16px;
    overflow: hidden;
    box-shadow: 0 10px 28px rgba(0,0,0,.25);
  }
  /* ---------- brand name ---------- */
  .brand {
    display: flex;
    align-items: center;
    gap: 10px;
    color: var(--ink);
    font-weight: 600;
    line-height: 1.15;
  }
  .brand__square { width: 14px; height: 14px; background: var(--brand-green); flex: none; }
  .brand__name { display: block; }
  .brand__sub { display: block; font-size: .32em; margin-top: 4px; }
  /* ---------- front ---------- */
  .card--front { left: 60px; top: 110px; background: var(--card-black); }
  .front-bands { position: absolute; inset: 0; width: 100%; height: 100%; }
  .card--front .brand { position: absolute; left: 150px; top: 18px; font-size: 30px; }
  .holder {
    position: absolute; left: 28px; top: 130px;
    color: var(--text-light); font-size: 19px; font-weight: 600;
  }
  .contact {
    position: absolute; color: var(--text-light);
    font-size: 12px; list-style: none; line-height: 1.5;
  }
  .contact li { display: flex; align-items: flex-start; gap: 8px; }
  .contact svg { width: 12px; height: 12px; flex: none; margin-top: 2px; fill: var(--text-light); }
  .contact--address { left: 28px; top: 170px; }
  .contact--address li + li { margin-top: 10px; }
  .contact--phones { right: 28px; top: 125px; }
  .contact--phones li + li { margin-top: 2px; }
  /* ---------- back ---------- */
  .card--back { left: 640px; top: 110px; background: var(--paper); display: flex; align-items: center; justify-content: center; }
  .card--back .brand { font-size: 34px; }
  /* ---------- presentation name ---------- */
  .showcase { position: absolute; left: 60px; top: 560px; font-size: 62px; gap: 16px; }
  .showcase .brand__square { width: 26px; height: 26px; }
</style>
</head>
<body>

<section class="card card--front" aria-label="Business card front">
  <svg class="front-bands" viewBox="0 0 500 286" preserveAspectRatio="none" aria-hidden="true">
    <polygon points="0,0 500,0 500,70 0,118" fill="var(--mist)"/>
    <polygon points="0,0 500,0 500,58 0,106" fill="var(--paper)"/>
    <polygon points="0,110 500,62 500,68 0,116" fill="var(--brand-yellow)"/>
  </svg>

  <div class="brand">
    <span class="brand__square"></span>
    <span><span class="brand__name">Summitrow</span><span class="brand__sub">Engineering &amp; Construction, Inc.</span></span>
  </div>

  <p class="holder">Neil Barton</p>

  <ul class="contact contact--address">
    <li>
      <svg viewBox="0 0 12 12"><path d="M6 0a4 4 0 0 0-4 4c0 3 4 8 4 8s4-5 4-8a4 4 0 0 0-4-4zm0 5.5A1.5 1.5 0 1 1 6 2.5a1.5 1.5 0 0 1 0 3z"/></svg>
      <span>4158 Harbor Vale Drive,<br>Lakemont, Ca 92018</span>
    </li>
    <li>
      <svg viewBox="0 0 12 12"><path d="M0 2h12v8H0zM1 3l5 4 5-4" stroke="var(--card-black)" stroke-width="1"/></svg>
      <span>nb@summitrowec.com</span>
    </li>
  </ul>

  <ul class="contact contact--phones">
    <li>
      <svg viewBox="0 0 12 12"><path d="M2.5 0.5l2 2.5-1 1.5c.8 1.6 2 2.8 3.6 3.6l1.5-1 2.5 2-1.2 2.2C5 11 1 7 .3 1.7z"/></svg>
      <span>714-555-0147</span>
    </li>
    <li>
      <svg viewBox="0 0 12 12"><path d="M3 0h6v12H3zM4 1.5v7.5h4V1.5z" fill-rule="evenodd"/></svg>
      <span>714-555-0192</span>
    </li>
    <li>
      <svg viewBox="0 0 12 12"><path d="M3 0h6v3H3zM0 4h12v6H9v2H3v-2H0zM4 8v3h4V8z" fill-rule="evenodd"/></svg>
      <span>714-555-0163</span>
    </li>
  </ul>
</section>

<section class="card card--back" aria-label="Business card back">
  <div class="brand">
    <span class="brand__square"></span>
    <span><span class="brand__name">Summitrow</span><span class="brand__sub">Engineering &amp; Construction, Inc.</span></span>
  </div>
</section>

<div class="brand showcase">
  <span class="brand__square"></span>
  <span><span class="brand__name">Summitrow</span><span class="brand__sub">Engineering &amp; Construction, Inc.</span></span>
</div>

</body>
</html>
```